Fallowmere community hall home page

We are building a modern, responsive website & booking system for our community hall. For this SketchHarbor task, we would like to receive design ideas for the home page.
There are no limits on the colours or fonts that can be used. We are looking for a modern, fresh design with a local/community feel. We don’t have a logo but we also recognise that our name is quite long! … So initials (FCH) instead of the name would be fine.
People book our community hall for a range of activities including: fitness classes, wedding receptions, birthday parties, business meetings, teaching, community events, charity fundraisers and other celebrations.
We have three main goals for the website. The first is that people can check our calendar and make a booking for an available time slot. The second is that they can read about our facilities and the prices for hiring them. The third is that people can find out about upcoming activities & events.
CTA: Book now
A button that links to a booking request form. (The form is not part of this design project)
Primary/Header navigation:
Home | Calendar | Facilities | Prices | Photos | News | Contact
Secondary/Footer navigation:
Chatterbook | Quipper
Login | Register | Privacy policy | Terms & conditions
Example texts (lorem ipsum etc. is also fine):
We have everything you need from a venue, whether it’s an elegant room with ample flexible space, a lavish and elegant hall for a wedding reception, a conference room that fits 125 delegates or a easy access venue to the town centre.
The hall is available for hire for wedding receptions, birthday celebrations, anniversaries, children's parties, presentations, lectures, fitness groups, and will comfortably accommodate all your guests.
This venue is well equipped with a modern kitchen, a range of audio and technical services, hearing loop, licensed bar, conference facilities, disabled access and unlimited free WiFi.
You can use this website to find out more about our rooms, equipment and the services we can offer and use the calendar to see where we have rooms available. You can also book rooms using our online booking system.
To the front of the building is a large public open grassed area across which is a row of shops. To the rear of the building is the large car park, including spaces for blue badge holders and a large enclosed cycle rack. This area also has extensive gardens, with seating and planting areas maintained by local volunteers.
The community hall is run and managed by volunteers of the Fallowmere Community Organisation. Our objectives are to increase opportunities for people living in and around Fallowmere.
We are passionate about being the heart of the community; caring for this community centred property and visitors are at the heart of all we do.
Where to go next
— Check when the hall is free
— Read our booking policy documents
— Make a booking reservation
Amenities
— Free WiFi
— Free car parking
— Fully equipped kitchen
— Hearing loop
Details for our most popular facilities (rooms):
Name: Main hall
Short description: A 127 square metre main hall with entrance lobby, toilets, a well-equipped kitchen and separate storage facilities. Three sets of double doors provide access to a large paved area and the adjacent playing field.
Capacity: 180 people
Price: £10-20 per hour
Links: More info | Book now
Name: Large meeting room
Short description: A delightful, spacious room with an outlook and access to the small walled garden. Ideal for meetings and small gatherings - it has its own access door and the use of a disabled W/C. We offer a reduced rate for this room when booked together with the main hall.
Capacity: 20 people
Price: £6-12 per hour
Attachments:
We have attached some photos of the hall & some (royalty free) stock images for inspiration.

```html
<!DOCTYPE html>
<html lang="en">
<head>
<meta charset="utf-8">
<title>Fallowmere community hall</title>
<link href="https://fonts.googleapis.com/css2?family=Merriweather:wght@300;400;700&family=Montserrat:wght@300;400;500&display=swap" rel="stylesheet">
<style>
  :root {
    --navy: #1c2b5a;
    --white: #ffffff;
    --text: #2b2b2b;
    --band: #f1f1f1;
  }
  * { margin: 0; padding: 0; box-sizing: border-box; }
  html, body { width: 900px; height: 1200px; overflow: hidden; background: var(--white); }
  body { position: relative; font-family: "Montserrat", sans-serif; color: var(--text); }

  .hero {
    position: absolute; left: 0; top: 0; width: 900px; height: 511px;
    background:
      radial-gradient(ellipse at 50% 30%, rgba(180,160,130,0.35), transparent 60%),
      linear-gradient(180deg, #3a3128 0%, #5e5647 35%, #8a8170 60%, #4a3d30 100%);
  }
  .hero::after {
    content: ""; position: absolute; inset: 0;
    background: linear-gradient(180deg, rgba(0,0,0,0.35), rgba(0,0,0,0.15) 40%, rgba(0,0,0,0.25));
  }
  .site-name {
    position: absolute; left: 34px; top: 21px; z-index: 2;
    font-family: "Montserrat", sans-serif; font-weight: 500; font-size: 13px;
    color: var(--white);
  }
  .main-nav { position: absolute; top: 21px; left: 0; width: 900px; height: 24px; z-index: 2; }
  .main-nav a {
    position: absolute; top: 0; font-size: 10.5px; color: var(--white);
    text-decoration: none; font-weight: 400;
  }
  .main-nav a.active::after {
    content: ""; position: absolute; left: 0; right: -3px; top: 20px; height: 1.5px; background: var(--white);
  }
  .hero-title {
    position: absolute; top: 164px; left: 0; width: 900px; z-index: 2; text-align: center;
    font-weight: 300; font-size: 44px; line-height: 56px; letter-spacing: 1.5px;
    color: var(--white); text-transform: uppercase;
  }
  .btn {
    position: absolute; top: 304px; width: 140px; height: 37px; border-radius: 19px; z-index: 2;
    display: flex; align-items: center; justify-content: center;
    font-size: 10px; font-weight: 500; letter-spacing: 1.8px; text-transform: uppercase; text-decoration: none;
  }
  .btn-book { left: 298px; background: var(--white); color: var(--navy); }
  .btn-info { left: 463px; border: 1.5px solid var(--white); color: var(--white); }

  .photo-cakes {
    position: absolute; left: 84px; top: 577px; width: 313px; height: 415px;
    background: linear-gradient(160deg, #6f8a52 0%, #c9a06a 35%, #e9b78f 55%, #b6c9c6 75%, #e3cde0 100%);
    box-shadow: 0 10px 24px rgba(0,0,0,0.12);
  }
  .photo-table {
    position: absolute; left: 218px; top: 778px; width: 204px; height: 272px;
    background: linear-gradient(170deg, #3c5b34 0%, #9b3b3f 25%, #eadfdc 50%, #f3f1ee 75%, #d9c3a7 100%);
    box-shadow: 0 10px 24px rgba(0,0,0,0.15);
  }
  .intro { position: absolute; left: 461px; top: 636px; width: 348px; }
  .intro h2 {
    font-family: "Merriweather", serif; font-weight: 400; font-size: 36px; line-height: 40px;
    color: var(--navy); margin-bottom: 24px;
  }
  .intro p { font-size: 10px; line-height: 19.8px; font-weight: 400; margin-bottom: 19.8px; }
  .intro p.narrow { width: 324px; }

  .more-band { position: absolute; left: 0; top: 1115px; width: 610px; height: 85px; background: var(--band); }
  .more-band h2 {
    position: absolute; left: 86px; top: 62px;
    font-family: "Merriweather", serif; font-weight: 400; font-size: 36px; color: var(--navy); white-space: nowrap;
  }
  .photo-party {
    position: absolute; left: 517px; top: 1175px; width: 383px; height: 25px;
    background: linear-gradient(90deg, #1d6f86, #3aa1b4 40%, #6f7f99 70%, #2c3f63);
  }
</style>
</head>
<body>
  <header class="hero" role="img" aria-label="Hall interior set for a reception with round tables, gold chairs and a chandelier">
    <div class="site-name">Fallowmere community hall</div>
    <nav class="main-nav">
      <a class="active" href="#" style="left:382px">Home</a>
      <a href="#" style="left:445px">Calendar</a>
      <a href="#" style="left:523px">Facilities</a>
      <a href="#" style="left:606px">Prices</a>
      <a href="#" style="left:679px">Photos</a>
      <a href="#" style="left:758px">News</a>
      <a href="#" style="left:826px">Contact</a>
    </nav>
    <h1 class="hero-title">We have everything<br>you need from a venue</h1>
    <a class="btn btn-book" href="#">Book now</a>
    <a class="btn btn-info" href="#">More info</a>
  </header>

  <div class="photo-cakes" role="img" aria-label="Cake stand with pastries and flowers at a garden party"></div>
  <div class="photo-table" role="img" aria-label="Table setting with crystal glasses, flowers and gold cutlery"></div>

  <section class="intro">
    <h2>Phasellus Sit Amet Massa Tincidunt</h2>
    <p>Whether it’s an elegant room with ample flexible space, a lavish and elegant hall for a wedding reception, a conference room that fits 125 delegates or a easy access venue to the town centre.</p>
    <p class="narrow">The hall is available for hire for wedding receptions, birthday celebrations, anniversaries, children's parties, presentations, lectures, fitness groups, and will comfortably accommodate all your guests.</p>
    <p class="narrow">This venue is well equipped with a modern kitchen, a range of audio and technical services, hearing loop, licensed bar, conference facilities, disabled access and unlimited free WiFi.</p>
  </section>

  <section class="more-band">
    <h2>Find Out More</h2>
  </section>
  <div class="photo-party" role="img" aria-label="Colourful party lights and confetti"></div>
</body>
</html>
```